Plakat-Design für Frauenfitnessstudio
Zielgruppe
Frauenfitnessstudio
Aufgabenstellung
Wir benötigen eine Außenplane die an der eingezeichneten Postion befestigt werden soll (Anhang 'Außenansicht').
Auf der Plane soll mindestens folgender Inhalt dargestellt werden:
- Logo
- Website 'morvenhalle-augsburg.de'
- Trelvano-Logo
- Pixomerat-Logo
Die Plane soll ab einer Reichweite von ca. 50 Metern erkennbar sein.
Die Maße betragen 480x280 cm.

```html
<!DOCTYPE html>
<html lang="de">
<head>
<meta charset="utf-8">
<title>Morvenhalle – Außenplane</title>
<link href="https://fonts.googleapis.com/css2?family=Oswald:wght@400;600&display=swap" rel="stylesheet">
<style>
  :root {
    --page-bg: #e9e9ea;
    --banner-dark: #45464a;
    --banner-mid: #7d7e83;
    --banner-light: #b4b5b9;
    --brand-yellow: #f5c518;
    --tag-white: #ffffff;
    --band-pink: #e8388f;
    --photo-skin: rgba(196, 150, 124, 0.55);
    --photo-pink: rgba(226, 96, 160, 0.55);
  }
  * { margin: 0; padding: 0; box-sizing: border-box; }
  html, body {
    width: 1200px; height: 675px; overflow: hidden;
    background: var(--page-bg);
  }
  .banner {
    position: absolute; left: 60px; top: 22px;
    width: 1080px; height: 630px;
    background: radial-gradient(ellipse at 48% 42%, var(--banner-light) 0%, var(--banner-mid) 50%, var(--banner-dark) 100%);
    overflow: hidden;
    font-family: "Oswald", "Arial Narrow", sans-serif;
  }
  .photo {
    position: absolute; top: 30px; bottom: 76px;
    background:
      radial-gradient(ellipse 45% 14% at 50% 34%, var(--photo-pink) 0%, rgba(226,96,160,0) 100%),
      radial-gradient(ellipse 40% 48% at 50% 48%, var(--photo-skin) 0%, rgba(196,150,124,0) 100%);
  }
  .photo--left { left: 40px; width: 360px; }
  .photo--right { left: 730px; width: 300px; }
  .logo {
    position: absolute; left: 360px; top: 175px; width: 400px;
    text-align: center;
  }
  .logo__name {
    color: var(--brand-yellow);
    font-weight: 600; font-size: 92px; letter-spacing: 3px;
    line-height: 0.98; text-transform: uppercase;
  }
  .tagline {
    position: absolute; left: 330px; top: 400px; width: 460px;
    color: var(--tag-white); font-weight: 400; font-size: 25px;
    line-height: 1.4; text-transform: uppercase; text-align: center;
  }
  .social {
    position: absolute; right: 18px; top: 16px;
    list-style: none;
    display: flex; flex-direction: column; align-items: flex-end; gap: 8px;
  }
  .social__item {
    display: flex; align-items: center; gap: 10px;
    color: var(--brand-yellow); font-size: 34px; font-weight: 600;
    line-height: 1.1;
  }
  .social__dot { width: 18px; height: 18px; background: var(--brand-yellow); }
  .web-band {
    position: absolute; left: 0; right: 0; bottom: 0; height: 76px;
    background: var(--band-pink);
    display: flex; align-items: center; justify-content: center;
  }
  .web-band__url {
    color: var(--tag-white); font-size: 44px; font-weight: 400;
    text-transform: uppercase; letter-spacing: 1px;
  }
</style>
</head>
<body>
  <main class="banner">
    <div class="photo photo--left" role="img" aria-label="Fotografie einer sportlichen Frau in pinkem Sport-Top, Rückenansicht"></div>
    <div class="photo photo--right" role="img" aria-label="Fotografie einer sportlichen Frau in pinkem Sport-Top, frontal"></div>

    <div class="logo">
      <p class="logo__name">Morven<br>halle</p>
    </div>

    <p class="tagline">Ihr Premiumstudio<br>Wohlfühl-Fitness für die Frau</p>

    <ul class="social">
      <li class="social__item"><span class="social__dot"></span>Trelvano</li>
      <li class="social__item"><span class="social__dot"></span>Pixomerat</li>
    </ul>

    <div class="web-band">
      <span class="web-band__url">www.morvenhalle-augsburg.de</span>
    </div>
  </main>
</body>
</html>
```